Commercial Construction Interior Fitout company needs Logo and Business Cards

We need a logo and business card design. We specialise in Commercial Ceilings, Partitions, Plastering and Carpentry.

Company name: 7QX Commercial Interiors. Would like a professional looking card more than a fancy look. Gloss front preferably black pattern with Fluro Green and white text.

Will need:

Name
Position
Phone
Fax
Email
Postal Address
Web address
Updates

Thank you so much everyone for your efforts and fantastic designs..   If I didn't respond to everyone personally,  my apologises. 

Again, thanks all

R.M                               

Target Market(s)

Existing & New clients in the Construction Industry

Industry/Entity Type

Business

Requirements
Nice to have
• 7QX to be overlapped or made into some sort of Logo

```html
<!DOCTYPE html>
<html lang="en">
<head>
<meta charset="utf-8">
<title>7QX Commercial Interiors – Business Card</title>
<link rel="stylesheet" href="https://fonts.googleapis.com/css2?family=Arimo:wght@400;700&display=swap">
<style>
  :root {
    --card-black: #07090a;
    --text-white: #ffffff;
    --brand-green: #66ff00;
    --accent-lime: #99ff33;
    --accent-bright: #66ff00;
    --accent-deep: #4ae800;
  }
  html, body {
    margin: 0;
    padding: 0;
    width: 1200px;
    height: 741px;
    overflow: hidden;
    background: var(--card-black);
  }
  .business-card {
    position: relative;
    width: 1200px;
    height: 741px;
    background: var(--card-black);
    font-family: "Arimo", Arial, sans-serif;
    overflow: hidden;
  }
  .corner-accent {
    position: absolute;
    top: 0;
    right: 0;
    width: 664px;
    height: 398px;
    background: radial-gradient(ellipse 100% 100% at 100% 0%,
      var(--accent-lime) 0%,
      var(--accent-bright) 35%,
      var(--accent-deep) 55%,
      rgba(7, 9, 10, 0) 100%);
  }
  .contact-details {
    position: absolute;
    left: 43px;
    top: 60px;
    margin: 0;
    padding: 0;
    list-style: none;
    color: var(--text-white);
    font-size: 44px;
    font-weight: 400;
    line-height: 59.5px;
    word-spacing: 6px;
  }
  .company-name {
    position: absolute;
    inset: 0;
    margin: 0;
    color: var(--brand-green);
    font-weight: 700;
    white-space: nowrap;
    line-height: 1;
    pointer-events: none;
  }
  .company-name .initials {
    position: absolute;
    left: 32px;
    top: 503px;
    font-size: 210px;
    letter-spacing: -3px;
  }
  .company-name .descriptor {
    position: absolute;
    left: 557px;
    top: 619px;
    font-size: 60px;
    letter-spacing: 1px;
  }
</style>
</head>
<body>
  <main class="business-card">
    <div class="corner-accent" role="img" aria-label="Decorative cluster of overlapping fluoro green blocks in the top right corner"></div>

    <ul class="contact-details">
      <li class="contact-name">Name</li>
      <li class="contact-position">Position</li>
      <li class="contact-phone">Phone</li>
      <li class="contact-fax">Fax</li>
      <li class="contact-email">Email</li>
      <li class="contact-postal">Postal Address</li>
      <li class="contact-web">Web Address</li>
    </ul>

    <h1 class="company-name">
      <span class="initials">7QX</span>
      <span class="descriptor">Commercial Interiors</span>
    </h1>
  </main>
</body>
</html>
```